Finish My Wordpress Site for Local Painting Company

The site is almost done, but I'm stuck and need expert assistance. Would love to work with someone over zoom so that I can express what I've been trying to accomplish and to learn more about the back end of Wordpress. Here's what's left to be done (I think):

Upload New Photos
Gallery (Before&After)
Anchors to: Get a Quote, Gallery
Font consistency
More padding at the bottom of pages?
Edit padding on Contact page?
Links (photos, buttons, social), add domains, edit page names
Normal entrance animation?
Mobile version

And here's the site as is:
http://kv4.c17.webvaultdemo.com/

Coding

Coded - Design and coding required

Number of Pages Required

1 page

Colors
0355a3

Requirements
Must have
• Communication between us as the work gets done

```html
<!DOCTYPE html>
<html lang="en">
<head>
<meta charset="utf-8">
<title>Ben Carver Painting</title>
<link href="https://fonts.googleapis.com/css2?family=Poppins:wght@500;600;700&family=Lato:ital,wght@0,400;0,700;1,400&display=swap" rel="stylesheet">
<style>
:root{
  --blue:#0355a3;
  --blue-deep:#1a3f95;
  --blue-dark:#16398a;
  --navy:#1e2f7a;
  --brown:#8a7360;
  --brown-band:#85705f;
  --pale:#dfe8f1;
  --white:#ffffff;
  --ink:#4a4a4a;
  --field:#4a4a4a;
  --star:#a08a76;
}
*{box-sizing:border-box;margin:0;padding:0}
html,body{width:1200px;height:3647px;overflow:hidden}
body{position:relative;font-family:'Lato',sans-serif;color:var(--ink);background:var(--white)}
.abs{position:absolute}
h1,h2,h3,.heading{font-family:'Poppins',sans-serif}

/* header */
.site-header{left:0;top:0;width:1200px;height:139px;background:linear-gradient(90deg,var(--blue-dark),var(--blue) 55%,var(--blue-deep));}
.logo-tab{left:0;top:0;width:1200px;height:178px;pointer-events:none}
.social{display:flex;gap:36px}
.social span{width:14px;height:14px;border-radius:50%;background:var(--white);display:block}
.phone{right:100px;top:22px;color:var(--white);font-family:'Poppins',sans-serif;font-weight:600;font-size:18px;display:flex;align-items:center;gap:8px}
.nav{top:78px;display:flex;gap:44px;font-family:'Lato',sans-serif;font-size:18px;color:var(--white);letter-spacing:.2px}
.nav .active{font-weight:700;position:relative}
.nav .active::after{content:"";position:absolute;left:12px;right:12px;bottom:-12px;height:3px;background:var(--white)}
.brand-mark{left:550px;top:8px;width:100px;height:100px;border-radius:50%;background:var(--white);border:4px solid var(--navy)}
.brand-name{left:470px;top:116px;width:260px;text-align:center;color:var(--white);font-family:'Poppins',sans-serif;font-weight:600;font-size:21px;line-height:24px}

/* hero */
.hero{left:0;top:139px;width:1200px;height:638px;background:linear-gradient(180deg,#5c9bd9 0%,#a9cdea 35%,#cfc9b4 55%,#6f9a3e 78%,#4f7f2a 100%)}
.hero-title{left:60px;top:322px;width:580px;text-align:center;font-family:'Poppins',sans-serif;font-weight:700;font-size:41px;line-height:45px;color:#1b2a55}
.btn{display:flex;align-items:center;justify-content:center;border-radius:30px;color:var(--white);font-family:'Poppins',sans-serif;font-weight:600;font-size:15px}
.btn-quote{left:158px;top:443px;width:180px;height:52px;background:var(--brown)}
.btn-upload{left:351px;top:443px;width:180px;height:52px;background:var(--blue)}
.arrow{width:52px;height:52px;border-radius:50%;background:rgba(255,255,255,.85);display:flex;align-items:center;justify-content:center}

/* about */
.about{left:0;top:777px;width:1200px;height:519px;background:var(--pale)}
.portrait{left:107px;top:837px;width:392px;height:392px;border-radius:50%;background:linear-gradient(160deg,#4b5a3c,#c9c3b8 60%,#efefef);border:16px solid var(--brown)}
.about-title{left:545px;top:866px;font-size:39px;font-weight:600;color:var(--blue)}
.about-text{left:547px;top:936px;width:565px;font-size:15.5px;line-height:27px;color:#555}
.about-text p+p{margin-top:6px}
.btn-more{left:542px;top:1132px;width:186px;height:63px;border:2px solid var(--navy);border-radius:32px;color:var(--navy);font-family:'Poppins',sans-serif;font-weight:600;font-size:17px;display:flex;align-items:center;justify-content:center}

/* services */
.section-title{width:1200px;left:0;text-align:center;font-family:'Poppins',sans-serif;font-weight:600;font-size:38px}
.services-title{top:1326px;color:var(--blue)}
.tile{top:1406px;height:278px;display:flex;align-items:center;justify-content:center;text-align:center;color:var(--white);font-family:'Poppins',sans-serif;font-weight:600;font-size:20px;line-height:25px;text-shadow:0 1px 3px rgba(0,0,0,.4)}
.arrow-side{width:40px;height:76px;background:rgba(255,255,255,.85);display:flex;align-items:center;justify-content:center}

/* gallery */
.gallery{left:0;top:1688px;width:1200px;height:467px;background:linear-gradient(90deg,var(--navy),var(--blue) 60%,var(--blue-deep))}
.gallery-title{top:1744px;color:var(--white)}
.shot{top:1824px;width:252px;height:228px;display:flex;align-items:flex-end;justify-content:center;padding-bottom:18px;color:var(--white);font-family:'Poppins',sans-serif;font-weight:700;font-size:22px}

/* reviews */
.reviews-title{top:2219px;color:var(--blue)}
.card{top:2315px;width:458px;height:226px;background:var(--white);border:2px solid #d8d8d8;border-radius:22px}
.card-back{background:var(--blue);border-radius:22px}
.avatar{width:78px;height:82px;border-radius:10px;background:linear-gradient(160deg,#cfc6bc,#5a4b42)}
.quote-mark{font-family:'Poppins',sans-serif;font-size:48px;color:var(--blue);line-height:1}
.review-text{width:262px;font-style:italic;font-size:14px;line-height:23px;color:#333}
.stars{display:flex;gap:4px}
.reviewer{font-weight:700;font-size:16px;color:var(--blue);letter-spacing:.5px}
.dot{width:15px;height:15px;border-radius:50%;border:2px solid var(--blue)}
.dot.on{background:var(--blue)}

/* quote */
.quote-band{left:0;top:2666px;width:1200px;height:580px;background:var(--brown-band)}
.quote-title{left:172px;top:2776px;font-size:38px;font-weight:600;color:var(--white)}
.contact-item{left:172px;color:var(--white);display:flex;gap:22px}
.contact-item .label{font-weight:700;font-size:17px;text-transform:uppercase}
.contact-item .value{font-size:17px;line-height:28px}
.field{left:557px;width:479px;background:var(--field);color:#ddd;font-size:15px;padding:12px 24px;border:1px solid #6a5e55}
.btn-submit{left:557px;top:3093px;width:192px;height:56px;border-radius:28px;background:var(--blue);color:var(--white);font-family:'Poppins',sans-serif;font-weight:600;font-size:20px;display:flex;align-items:center;justify-content:center}

/* footer */
.footer{left:0;top:3246px;width:1200px;height:334px;background:var(--blue)}
.foot-col{top:3326px;color:var(--white)}
.foot-col h3{font-size:22px;font-weight:600;margin-bottom:14px}
.foot-col li{list-style:none;font-size:15px;line-height:33px}
.foot-col p{font-size:15px;line-height:29px}
.sub-input{left:798px;top:3370px;width:270px;height:44px;background:#2d66b8;color:#e6eefb;font-size:15px;padding:12px 20px}
.sub-btn{left:798px;top:3428px;width:270px;height:45px;background:var(--brown);color:var(--white);font-family:'Poppins',sans-serif;font-weight:600;font-size:16px;display:flex;align-items:center;justify-content:center}
.bottom-bar{left:0;top:3580px;width:1200px;height:67px;background:var(--blue-dark)}
.copyright{left:0;top:3605px;width:1200px;text-align:center;font-size:14px;color:#d8e2f3}
</style>
</head>
<body>

<header>
  <div class="abs site-header"></div>
  <svg class="abs logo-tab" viewBox="0 0 1200 178"><polygon points="474,139 729,139 692,178 510,178" fill="#1e48a0"/></svg>
  <div class="abs social" style="left:112px;top:26px"><span></span><span></span><span></span></div>
  <div class="abs phone">
    <svg width="26" height="22" viewBox="0 0 26 22" fill="none" stroke="#fff" stroke-width="2"><path d="M5 2l4 4-2 3c1 3 4 6 7 7l3-2 4 4-3 3C10 21 2 13 3 5z"/><path d="M15 2a7 7 0 0 1 7 7M15 6a3 3 0 0 1 3 3"/></svg>
    (555) 014-2286
  </div>
  <nav class="abs nav" style="left:107px"><span class="active">HOME</span><span>ABOUT US</span><span>OUR SERVICES</span></nav>
  <nav class="abs nav" style="left:716px"><span>OUR GALLERY</span><span>BLOGS</span><span>CONTACT US</span></nav>
  <div class="abs brand-mark"></div>
  <div class="abs brand-name">BEN CARVER<br>PAINTING</div>
</header>

<section>
  <div class="abs hero" role="img" aria-label="Freshly painted two-storey house with green lawn under blue sky"></div>
  <h1 class="abs hero-title">Where preparation makes all the difference.</h1>
  <div class="abs btn btn-quote">GET A QUOTE</div>
  <div class="abs btn btn-upload">UPLOAD PHOTOS</div>
  <div class="abs arrow" style="left:31px;top:370px"><svg width="14" height="22"><path d="M11 2L3 11l8 9" stroke="#222" stroke-width="2.5" fill="none"/></svg></div>
  <div class="abs arrow" style="left:1117px;top:370px"><svg width="14" height="22"><path d="M3 2l8 9-8 9" stroke="#222" stroke-width="2.5" fill="none"/></svg></div>
</section>

<section>
  <div class="abs about"></div>
  <div class="abs portrait" role="img" aria-label="Portrait of the company founder wearing a dust mask"></div>
  <h2 class="abs about-title">Ben Carver Painting</h2>
  <div class="abs about-text">
    <p>I'm Sam Whitlock, and I founded Ben Carver Painting over 30 years ago. Since then, we've made it our mission to provide expert painting services.</p>
    <p>We believe that the key to a great painting job is preparation, so we pride ourselves on thorough prep work and inspections before even a drop of paint touches your home. We do everything we can to address any issues that may arise and continue to tailor our plans to meet your ever-changing needs.</p>
  </div>
  <div class="abs btn-more">READ MORE</div>
</section>

<section>
  <h2 class="abs section-title services-title">Our Services</h2>
  <div class="abs tile" style="left:0;width:293px;background:linear-gradient(160deg,#e9eaea,#9a9c9c)" role="img" aria-label="White kitchen cabinets">Kitchen Cabinets</div>
  <div class="abs tile" style="left:297px;width:298px;background:linear-gradient(160deg,#c9a57d,#6e5845)" role="img" aria-label="Hands working on timber">Carpentry</div>
  <div class="abs tile" style="left:600px;width:298px;background:linear-gradient(160deg,#8a6a4a,#4d3826)" role="img" aria-label="Textured decorative wall finish">Faux &amp; Decorative<br>Finishes</div>
  <div class="abs tile" style="left:902px;width:298px;background:linear-gradient(160deg,#7aa2d6,#c9cdd3 60%,#8f3d24)" role="img" aria-label="Modern commercial building facade">Commercial</div>
  <div class="abs arrow-side" style="left:0;top:1514px;border-radius:0 38px 38px 0"><svg width="12" height="20"><path d="M10 2L2 10l8 8" stroke="#222" stroke-width="2.5" fill="none"/></svg></div>
  <div class="abs arrow-side" style="left:1160px;top:1514px;border-radius:38px 0 0 38px"><svg width="12" height="20"><path d="M2 2l8 8-8 8" stroke="#222" stroke-width="2.5" fill="none"/></svg></div>
</section>

<section>
  <div class="abs gallery"></div>
  <h2 class="abs section-title gallery-title">Our Gallery</h2>
  <div class="abs shot" style="left:74px;background:linear-gradient(180deg,#b9c7c4,#e5e5e2 45%,#4f6a3a)" role="img" aria-label="White colonial house before painting">BEFORE</div>
  <div class="abs shot" style="left:334px;background:linear-gradient(180deg,#8a97a0,#dfe2de 45%,#3f5431)" role="img" aria-label="White colonial house after painting">AFTER</div>
  <div class="abs shot" style="left:604px;background:linear-gradient(180deg,#9ab9da,#4b5666 50%,#363d45)" role="img" aria-label="Victorian house before painting">BEFORE</div>
  <div class="abs shot" style="left:865px;background:linear-gradient(180deg,#8fb0d4,#356b6a 50%,#2c3f3e)" role="img" aria-label="Victorian house after painting">AFTER</div>
  <svg class="abs" style="left:30px;top:1915px" width="24" height="40"><path d="M20 3L4 20l16 17" stroke="#fff" stroke-width="4" fill="none"/></svg>
  <svg class="abs" style="left:1134px;top:1915px" width="24" height="40"><path d="M4 3l16 17-16 17" stroke="#fff" stroke-width="4" fill="none"/></svg>
</section>

<section>
  <h2 class="abs section-title reviews-title">Latest Reviews</h2>
  <div class="abs card-back" style="left:117px;top:2303px;width:290px;height:226px"></div>
  <div class="abs card-back" style="left:790px;top:2328px;width:290px;height:220px"></div>
  <div class="abs card" style="left:133px"></div>
  <div class="abs card" style="left:608px"></div>

  <div class="abs avatar" style="left:167px;top:2350px" role="img" aria-label="Reviewer photo"></div>
  <div class="abs quote-mark" style="left:256px;top:2348px">“</div>
  <p class="abs review-text" style="left:297px;top:2351px">Pellentesque faucibus Ut accumsan ultricies elit Maecenas at justo id velit placerat molestie Donec dictum lectus non odio Cras a ante vitae enim</p>
  <div class="abs stars" style="left:297px;top:2451px">
    <svg width="110" height="20" viewBox="0 0 110 20" fill="#a08a76"><g id="st"><polygon points="10,1 12.6,7 19,7.4 14,11.6 15.6,18 10,14.4 4.4,18 6,11.6 1,7.4 7.4,7"/></g><use href="#st" x="22"/><use href="#st" x="44"/><use href="#st" x="66"/><use href="#st" x="88"/></svg>
  </div>
  <div class="abs reviewer" style="left:297px;top:2482px">MARIA K.</div>

  <div class="abs avatar" style="left:638px;top:2348px" role="img" aria-label="Reviewer photo"></div>
  <div class="abs quote-mark" style="left:727px;top:2346px">“</div>
  <p class="abs review-text" style="left:768px;top:2349px">Pellentesque faucibus Ut accumsan ultricies elit Maecenas at justo id velit placerat molestie Donec dictum lectus non odio Cras a ante vitae enim</p>
  <div class="abs stars" style="left:766px;top:2449px">
    <svg width="110" height="20" viewBox="0 0 110 20" fill="#a08a76"><use href="#st"/><use href="#st" x="22"/><use href="#st" x="44"/><use href="#st" x="66"/><use href="#st" x="88"/></svg>
  </div>
  <div class="abs reviewer" style="left:768px;top:2480px">OWEN T.</div>

  <div class="abs dot" style="left:567px;top:2575px"></div>
  <div class="abs dot on" style="left:592px;top:2575px"></div>
  <div class="abs dot" style="left:617px;top:2575px"></div>
</section>

<section>
  <div class="abs quote-band"></div>
  <h2 class="abs quote-title">Get a Quote</h2>
  <div class="abs contact-item" style="top:2864px">
    <svg width="42" height="42" viewBox="0 0 42 42" fill="none" stroke="#fff" stroke-width="1.6"><path d="M21 38s-12-12-12-21a12 12 0 0 1 24 0c0 9-12 21-12 21z"/><circle cx="21" cy="17" r="4.5"/><path d="M6 36c4 3 26 3 30 0"/></svg>
    <div><div class="label">Address</div><div class="value">418 Elmwood Ave, 2B<br>Fairview, MA 01999</div></div>
  </div>
  <div class="abs contact-item" style="top:2975px">
    <svg width="42" height="42" viewBox="0 0 42 42" fill="none" stroke="#fff" stroke-width="1.6"><path d="M8 4l7 7-4 5c2 6 8 12 14 14l5-4 7 7-5 5C18 37 5 24 4 9z"/></svg>
    <div><div class="label">Phone Number</div><div class="value">(555) 014-2286</div></div>
  </div>
  <div class="abs contact-item" style="top:3066px">
    <svg width="42" height="36" viewBox="0 0 42 36" fill="none" stroke="#fff" stroke-width="1.6"><rect x="3" y="6" width="36" height="26"/><path d="M3 6l18 15L39 6M3 32l13-12M39 32L26 20"/></svg>
    <div><div class="label">Email Address</div><div class="value">sam@bencarverpainting.example</div></div>
  </div>
  <div class="abs field" style="top:2788px;height:46px">Name</div>
  <div class="abs field" style="top:2845px;height:46px">Email address</div>
  <div class="abs field" style="top:2902px;height:46px">Phone</div>
  <div class="abs field" style="top:2959px;height:114px">Message</div>
  <div class="abs btn-submit">SUBMIT</div>
</section>

<footer>
  <div class="abs footer"></div>
  <div class="abs foot-col" style="left:164px"><h3>Company</h3><ul><li>About Us</li><li>Services</li><li>Gallery</li><li>Blogs</li></ul></div>
  <div class="abs foot-col" style="left:355px;top:3328px"><h3>Resources</h3><ul><li>Reviews</li><li>Get a Quote</li><li>Sitemap</li><li>Contact</li></ul></div>
  <div class="abs foot-col" style="left:553px;top:3328px"><h3>Contact Us</h3><p>418 Elmwood Ave, 2B<br>Fairview, MA 01999</p><p style="margin-top:8px">92 Linden Street, #6<br>Brookdale, MA 01998</p></div>
  <div class="abs foot-col" style="left:793px;top:3324px"><h3>Subscribe newsletter</h3></div>
  <div class="abs sub-input">Email address</div>
  <div class="abs sub-btn">SUBSCRIBE</div>
  <div class="abs bottom-bar"></div>
  <div class="abs copyright">© 2020 Company Name | All Rights Reserved</div>
  <div class="abs social" style="left:968px;top:3612px;gap:22px"><span></span><span></span><span></span></div>
</footer>

</body>
</html>
```